Author and Publisher

Cover for a book on the process of publishing a book from the presentation to the publisher until the selling in bookstores :
A behind-the-scenes journey through the world of book publishing, from manuscript to bookstore. The book explores the relationship between authors and publishers, manuscript selection, contracts, editing, proofreading, book design, printing, distribution, bookstores and online sales. It reveals the many people, decisions and processes involved in turning a text into a physical book and bringing it to readers. The illustration should evoke publishing as a lively, contemporary ecosystem, combining creativity, craftsmanship, business and the enduring appeal of books.
FORMAT : 14 x 20,5 cm
AUTHOR : Luc Varennes
TITLE : Le scribe et la presse
PUBLISHER : Editions Trovel (at the bottom of the page)
Target Market(s)
General public, mainly news authors of books
Look and feel
Each slider illustrates characteristics of the customer's brand and the style your logo design should communicate.

```html
<!DOCTYPE html>
<html lang="fr">
<head>
<meta charset="utf-8">
<title>Le scribe et la presse — couverture</title>
<link rel="stylesheet" href="https://fonts.googleapis.com/css2?family=Jost:wght@300;400&family=Playfair+Display:wght@800;900&display=swap">
<style>
  :root {
    --page-bg: #ffffff;
    --back-cream: #f5ede4;
    --ink-teal: #123b4b;
    --rust: #b4431e;
    --body-ink: #2a2a2a;
    --white: #ffffff;
    --wall-light: #ebe7e3;
    --wall-warm: #d8cfc6;
    --desk-wood: #6b4428;
    --desk-dark: #3e2716;
  }
  * { margin: 0; padding: 0; box-sizing: border-box; }
  html, body {
    width: 1200px; height: 557px; overflow: hidden;
    background: var(--page-bg);
  }
  .cover-spread {
    position: absolute;
    left: 245px; top: 28px;
    width: 710px; height: 502px;
    display: flex;
    box-shadow: 2px 3px 5px rgba(0,0,0,0.25);
  }
  .back-cover {
    width: 342px; height: 100%;
    background: var(--back-cream);
    padding: 67px 42px 0 39px;
  }
  .back-cover .blurb {
    font-family: 'Jost', sans-serif;
    font-weight: 300;
    font-size: 10.3px;
    line-height: 12.45px;
    color: var(--body-ink);
    text-align: justify;
    margin-bottom: 12.45px;
  }
  .spine {
    width: 25px; height: 100%;
    background: var(--ink-teal);
    position: relative;
    color: var(--white);
  }
  .spine > * {
    position: absolute;
    left: 50%;
    transform-origin: 0 0;
    transform: rotate(90deg) translateY(-50%);
    white-space: nowrap;
  }
  .spine-author {
    top: 38px;
    font-family: 'Jost', sans-serif; font-weight: 300;
    font-size: 9px; letter-spacing: 3px;
  }
  .spine-title {
    top: 192px;
    font-family: 'Playfair Display', serif; font-weight: 800;
    font-size: 15px;
  }
  .spine-publisher {
    top: 418px;
    font-family: 'Jost', sans-serif; font-weight: 300;
    font-size: 10px;
  }
  .front-cover {
    width: 343px; height: 100%;
    position: relative;
    overflow: hidden;
  }
  .front-illustration {
    position: absolute; inset: 0;
    background:
      linear-gradient(180deg, var(--wall-warm) 0%, var(--wall-light) 30%, var(--wall-light) 55%, #ddd2c6 68%, var(--desk-wood) 80%, var(--desk-dark) 100%);
  }
  .front-author {
    position: absolute; top: 34px; left: 0; right: 0;
    text-align: center;
    font-family: 'Jost', sans-serif; font-weight: 400;
    font-size: 11.5px; letter-spacing: 3px;
    color: var(--ink-teal);
  }
  .front-title {
    position: absolute; top: 62px; left: 0; right: 0;
    text-align: center;
    font-family: 'Playfair Display', serif; font-weight: 900;
    letter-spacing: -1.5px;
  }
  .front-title .line-one {
    display: block;
    font-size: 50px; line-height: 50px;
    color: var(--ink-teal);
  }
  .front-title .line-two {
    display: block;
    font-size: 44px; line-height: 46px;
    color: var(--rust);
  }
  .front-title .connector { font-size: 28px; margin-right: 6px; }
  .front-publisher {
    position: absolute; bottom: 20px; left: 0; right: 0;
    text-align: center;
    font-family: 'Jost', sans-serif; font-weight: 300;
    font-size: 13px;
    color: var(--white);
  }
</style>
</head>
<body>
  <main class="cover-spread">
    <section class="back-cover">
      <p class="blurb">Lorem ipsum dolor sit amet, consectetuer adipiscing elit, sed diam nonummy nibh euismod tincidunt ut laoreet dolore magna aliquam erat volutpat. Ut wisi enim ad minim veniam, quis. Lorem ipsum dolor sit amet, consectetuer adipiscing elit, sed diam nonummy nibh euismod tincidunt ut laoreet dolore magna aliquam erat volutpat. Ut wisi enim ad minim veniam, quis.</p>
      <p class="blurb">Lorem ipsum dolor sit amet, consectetuer adipiscing elit, sed diam nonummy nibh euismod tincidunt ut laoreet dolore magna aliquam erat volutpat. Ut wisi enim ad minim veniam, quis. Lorem ipsum dolor sit amet, consectetuer adipiscing elit, sed diam nonummy nibh euismod tincidunt ut laoreet dolore magna aliquam erat volutpat. Ut wisi enim ad minim veniam, quis.</p>
      <p class="blurb">Lorem ipsum dolor sit amet, consectetuer adipiscing elit, sed diam nonummy nibh euismod tincidunt ut laoreet dolore magna aliquam erat volutpat. Ut wisi enim ad minim veniam, quis. Lorem ipsum dolor sit amet, consectetuer adipiscing elit, sed diam nonummy nibh euismod tincidunt ut laoreet dolore magna aliquam erat volutpat. Ut wisi enim ad minim veniam, quis.</p>
    </section>

    <aside class="spine">
      <span class="spine-author">LUC VARENNES</span>
      <span class="spine-title">Le scribe et la presse</span>
      <span class="spine-publisher">Editions Trovel</span>
    </aside>

    <section class="front-cover">
      <div class="front-illustration" role="img" aria-label="Sunlit desk with an open laptop releasing a stream of flying manuscript pages that turn into a stack of books, a pen pot and small books on a wooden table against a pale wall with leaf shadows"></div>
      <p class="front-author">LUC VARENNES</p>
      <h1 class="front-title">
        <span class="line-one">Le scribe</span>
        <span class="line-two"><span class="connector">et</span>la presse</span>
      </h1>
      <p class="front-publisher">Editions Trovel</p>
    </section>
  </main>
</body>
</html>
```